Business Card

We need a business card designed using one of the attached logo designs (our preference is for the boxes version, but if you think it looks better with the horizontal version we will consider those too). Standard business card dimensions.

Details that need to be included:

Lewis Marsh
Quorvane S.L.U
lewis@quorvane.com

Phone numbers:
(UK) +44 731 4602 385
(Spain) +34 615 480 327

Twitter: @Quorvane
Web: http://www.quorvane.com

Tagline (optional, if it doesnt make it look too cluttered):
Automation and configuration management specialists
or
Configuration management specialists

```html
<!DOCTYPE html>
<html lang="en">
<head>
<meta charset="utf-8">
<title>Quorvane S.L.U – Business Card</title>
<link rel="stylesheet" href="https://fonts.googleapis.com/css2?family=Arimo:wght@400;700&display=swap">
<style>
  :root {
    --page: #ffffff;
    --card: #ffffff;
    --ink: #111416;
    --brand-cyan: #5ce2f6;
    --brand-blue: #5ab4f7;
    --shadow: rgba(0, 0, 0, 0.18);
  }
  html, body {
    margin: 0;
    padding: 0;
    width: 1200px;
    height: 900px;
    overflow: hidden;
    background: var(--page);
    font-family: "Arimo", Arial, sans-serif;
    color: var(--ink);
  }
  .card {
    position: absolute;
    left: 40px;
    top: 85px;
    width: 1118px;
    height: 723px;
    background: var(--card);
    box-shadow: 0 10px 18px var(--shadow);
  }
  .brand-mark {
    position: absolute;
    left: 72px;
    top: 130px;
    width: 298px;
    height: 298px;
    border-radius: 24px;
    background: linear-gradient(45deg, var(--brand-blue), var(--brand-cyan));
  }
  .brand-name {
    position: absolute;
    left: 64px;
    top: 438px;
    width: 320px;
    margin: 0;
    font-size: 50px;
    font-weight: 700;
    letter-spacing: 2px;
    color: var(--ink);
    white-space: nowrap;
  }
  .identity {
    position: absolute;
    right: 71px;
    top: 128px;
    text-align: right;
  }
  .identity .company {
    margin: 0;
    font-size: 39px;
    font-weight: 700;
    line-height: 44px;
  }
  .identity .person {
    margin: 8px 0 0;
    font-size: 80px;
    font-weight: 700;
    line-height: 82px;
    color: var(--brand-cyan);
  }
  .identity .email {
    margin: 0;
    font-size: 35px;
    line-height: 44px;
  }
  .contacts {
    position: absolute;
    top: 580px;
    margin: 0;
    font-size: 33px;
    line-height: 45px;
    white-space: nowrap;
  }
  .contacts.phones { left: 63px; }
  .contacts.online { left: 650px; }
  .contacts strong { font-weight: 700; }
  .contacts p { margin: 0; }
</style>
</head>
<body>
  <main class="card">
    <div class="brand-mark" aria-hidden="true"></div>
    <p class="brand-name">QUORVANE</p>

    <header class="identity">
      <p class="company">QUORVANE S.L.U</p>
      <h1 class="person">LEWIS MARSH</h1>
      <p class="email">lewis@quorvane.com</p>
    </header>

    <section class="contacts phones">
      <p><strong>UK</strong> +44 731 4602 385</p>
      <p><strong>Spain</strong> +34 615 480 327</p>
    </section>

    <section class="contacts online">
      <p><strong>Twitter</strong> @quorvane</p>
      <p><strong>Web</strong> www.quorvane.com</p>
    </section>
  </main>
</body>
</html>
```